Business Card Design Project

We are rebranding an existing automotive collision repair business. The business is called dentworks garage. I have attached logo but I'm not tied to that. I want to leave this wide open.

I want this card to say we are professional, competent, cutting edge. We are focused on customers and use a lot of the latest technology to make the customer experience different. We sign customers in on iPads. Paperwork I signed electronically and updates are sent via text, email, logging on a website or as they wish. I want this innovation and image to come through in our cards

Target Market(s)

60%. Women 40% men. Age 35-60

Industry/Entity Type

Automotive

Requirements
Must have
• The card must have name, title, phone,email, cell, web page

```html
<!DOCTYPE html>
<html lang="en">
<head>
<meta charset="utf-8">
<title>Dentworks Garage – Business Card</title>
<link href="https://fonts.googleapis.com/css2?family=Ubuntu:wght@400;500;700&display=swap" rel="stylesheet">
<style>
  :root {
    --stage: #2e2e2e;
    --card-white: #ffffff;
    --card-shade: #ececec;
    --brand-green: #8dbb1e;
    --ink: #4a4a4a;
    --ink-soft: #6a6a6a;
    --rule: #b9d46a;
    --amber-deep: #e07a00;
    --amber: #f6a400;
    --amber-light: #ffd24a;
  }
  * { box-sizing: border-box; margin: 0; padding: 0; }
  html, body {
    width: 1200px; height: 901px; overflow: hidden;
    background: var(--stage);
    font-family: "Ubuntu", sans-serif;
  }
  .canvas {
    width: 1200px; height: 901px;
    display: flex; align-items: center; justify-content: center; gap: 60px;
  }
  .card {
    width: 530px; height: 303px;
    border-radius: 24px;
    overflow: hidden;
    position: relative;
    box-shadow: 0 12px 30px rgba(0,0,0,0.45);
  }

  /* Back of card */
  .card--back { background: var(--card-white); }
  .back-art {
    position: absolute; inset: 0;
    background:
      radial-gradient(ellipse at 30% 45%, var(--amber-light) 0%, rgba(255,210,74,0) 45%),
      linear-gradient(120deg, rgba(255,255,255,1) 0%, rgba(255,255,255,0) 28%),
      linear-gradient(160deg, var(--amber-deep) 0%, var(--amber) 50%, var(--amber-light) 100%);
  }
  .back-name {
    position: absolute; left: 0; right: 0; top: 126px;
    text-align: center;
    color: var(--card-white);
    font-weight: 700; font-size: 40px; letter-spacing: -0.5px;
  }

  /* Front of card */
  .card--front {
    background: linear-gradient(180deg, var(--card-white) 0%, var(--card-shade) 100%);
    color: var(--ink);
  }
  .front-name {
    position: absolute; left: 40px; top: 50px;
    color: var(--brand-green);
    font-weight: 700; font-size: 32px; letter-spacing: -0.5px;
  }
  .header-rule {
    position: absolute; left: 40px; right: 40px; top: 100px;
    height: 2px; background: var(--rule);
  }
  .person { position: absolute; left: 40px; top: 130px; }
  .person__name { color: var(--brand-green); font-size: 22px; font-weight: 500; }
  .person__title { color: var(--ink-soft); font-size: 17px; margin-top: 6px; }
  .person-rule {
    position: absolute; left: 40px; top: 196px;
    width: 205px; height: 2px; background: var(--rule);
  }
  .contact { list-style: none; font-size: 17px; line-height: 28px; white-space: nowrap; }
  .contact__label { color: var(--brand-green); display: inline-block; width: 20px; }
  .contact--phones { position: absolute; left: 40px; top: 208px; }
  .contact--online { position: absolute; left: 272px; top: 160px; font-size: 15px; }
</style>
</head>
<body>
  <main class="canvas">
    <section class="card card--back" aria-label="Card back">
      <div class="back-art" role="img" aria-label="Abstract amber light streaks and glowing tech shapes"></div>
      <div class="back-name">Dentworks Garage</div>
    </section>

    <section class="card card--front" aria-label="Card front">
      <div class="front-name">Dentworks Garage</div>
      <div class="header-rule"></div>

      <div class="person">
        <div class="person__name">Mara Tellwood</div>
        <div class="person__title">Managing Director</div>
      </div>
      <div class="person-rule"></div>

      <ul class="contact contact--phones">
        <li><span class="contact__label">p</span>7301 462 918</li>
        <li><span class="contact__label">c</span>6124 039 587</li>
      </ul>

      <ul class="contact contact--online">
        <li><span class="contact__label">e</span>info@dentworksgarage.com</li>
        <li><span class="contact__label">w</span>www.dentworksgarage.com</li>
      </ul>
    </section>
  </main>
</body>
</html>
```